Larder & Flame - Premium Catering needs a new menu design.

I currently use menupro to make my own menus for printing and uploading to the website (PDF). I need a professional menu to replace my current menu. I wold like to mail these menus out so I'm thinking a tri-fold menu would be the best option. Similar to what pizzerias send out.

Logo Text

Would be good to reduce the text thickness of the letters "MIL" in the word MILLRUN. Right now MIL has thicker text.

Colors

Designer to choose colors to be used in the design.

```html
<!DOCTYPE html>
<html lang="en">
<head>
<meta charset="utf-8">
<title>Millrun Deli – Breakfast Menu</title>
<link href="https://fonts.googleapis.com/css2?family=Fira+Sans+Condensed:wght@400;500;600;700&display=swap" rel="stylesheet">
<style>
  :root{
    --backdrop:#585858;
    --paper:#ffffff;
    --gold:#b8963a;
    --maroon:#7b1a1f;
    --ink:#1c1c1c;
  }
  *{box-sizing:border-box;margin:0;padding:0}
  html,body{width:1200px;height:1200px;overflow:hidden;background:var(--backdrop)}
  body{font-family:"Fira Sans Condensed",sans-serif;position:relative}
  .menu-sheet{position:absolute;left:155px;top:25px;width:890px;height:1150px;background:var(--paper)}
  .menu-frame{position:absolute;left:15px;top:14px;width:860px;height:1121px;border:2px solid var(--gold)}

  .banner{position:absolute;display:flex;align-items:center;justify-content:center;gap:6px;
    color:var(--gold);font-weight:600;letter-spacing:2px;line-height:38px;height:38px;white-space:nowrap}
  .banner::before,.banner::after{content:"";display:block;height:4px;background:var(--gold);width:24px;flex:none}
  .banner-note{position:absolute;text-align:center;color:var(--gold);font-size:11.5px;font-weight:500;line-height:15px;white-space:nowrap}

  .section-rule{position:absolute;height:2px;background:var(--gold)}
  .dash{position:absolute;border-top:1.6px dashed var(--gold)}
  .section-title{position:absolute;display:flex;align-items:center;justify-content:center;gap:10px;
    color:var(--maroon);font-size:27px;font-weight:600;line-height:30px;height:30px;letter-spacing:.5px}
  .flourish{display:inline-block;width:16px;height:12px;border-radius:6px;background:var(--maroon);opacity:.55}

  .left{left:51px;width:367px}
  .right{left:472px;width:368px}

  .item{position:absolute;display:flex;align-items:center;height:24px;line-height:24px;color:var(--maroon)}
  .item .name{font-size:20.5px;font-weight:500;white-space:nowrap}
  .item .leader{flex:1;height:1px;background:var(--gold);margin:0 6px 0 5px}
  .item .price{font-size:13.5px;font-weight:700;white-space:nowrap;letter-spacing:.3px}
  .item.minor{color:var(--gold)}
  .item.minor .name{font-size:12px;font-weight:500}
  .item.minor .price{color:var(--maroon)}
  .item.size{color:var(--gold);height:16px;line-height:16px}
  .item.size .name{font-size:12px;font-weight:700}
  .item.size .price{color:var(--maroon)}
  .detail{position:absolute;font-size:11px;font-weight:500;color:var(--ink);line-height:14px;white-space:nowrap}
  .inline-detail{font-size:11px;font-weight:500;color:var(--ink);margin-left:6px}
  .note{position:absolute;color:var(--gold);font-size:11.5px;font-weight:500;line-height:14px;white-space:nowrap}

  .column-divider{position:absolute;left:445px;top:190px;height:912px;border-left:1.6px dashed var(--gold)}
  .order-online{position:absolute;left:337px;width:214px;top:1111px;text-align:center;color:var(--gold);font-size:12px;font-weight:500;line-height:14px}
  .order-bracket{position:absolute;left:337px;width:214px;top:1124px;height:5px;border:1.5px solid var(--gold);border-top:none}
</style>
</head>
<body>
<main class="menu-sheet">
  <div class="menu-frame"></div>

  <h1 class="banner" style="left:0;width:890px;top:34px;font-size:38px;">BREAKFAST</h1>
  <p class="banner-note" style="left:0;width:890px;top:74px;font-size:13px;">SERVED ALL DAY</p>

  <!-- Sandwiches -->
  <div class="section-rule left" style="top:102px"></div>
  <h2 class="section-title left" style="top:117px"><span class="flourish" role="img" aria-label="scroll flourish"></span>SANDWICHES<span class="flourish" role="img" aria-label="scroll flourish"></span></h2>
  <div class="section-rule left" style="top:163px"></div>

  <div class="dash left" style="top:189px"></div>
  <div class="item left" style="top:198px"><span class="name">2 Jumbo Eggs</span><span class="leader"></span><span class="price">$ 2.59</span></div>
  <div class="dash left" style="top:229px"></div>
  <div class="item left" style="top:239px"><span class="name">2 Jumbo Eggs with Cheese</span><span class="leader"></span><span class="price">$ 3.09</span></div>
  <div class="dash left" style="top:271px"></div>
  <div class="item left" style="top:277px"><span class="name">2 Jumbo Eggs with Meat</span><span class="leader"></span><span class="price">$ 4.09</span></div>
  <p class="detail" style="left:65px;top:301px">Pork roll, sausage, or bacon.</p>
  <div class="dash left" style="top:317px"></div>
  <div class="item left" style="top:324px"><span class="name">2 Jumbo Eggs with Meat &amp; Cheese</span><span class="leader"></span><span class="price">$ 4.59</span></div>
  <p class="detail" style="left:65px;top:347px">Pork roll, sausage, or bacon.</p>
  <div class="dash left" style="top:364px"></div>

  <!-- Platters -->
  <div class="section-rule left" style="top:389px"></div>
  <h2 class="section-title left" style="top:405px"><span class="flourish" role="img" aria-label="scroll flourish"></span>PLATTERS<span class="flourish" role="img" aria-label="scroll flourish"></span></h2>
  <div class="section-rule left" style="top:450px"></div>

  <div class="dash left" style="top:475px"></div>
  <div class="item left" style="top:482px"><span class="name">2 Jumbo Eggs Any Style</span><span class="leader"></span><span class="price">$ 5.99</span></div>
  <p class="detail" style="left:65px;top:505px">Served with home fries and toast.</p>
  <div class="dash left" style="top:522px"></div>
  <div class="item left" style="top:529px"><span class="name">2 Jumbo Eggs Any Style with Meat</span><span class="leader"></span><span class="price">$ 7.99</span></div>
  <p class="detail" style="left:65px;top:552px">Served with home fries and toast.</p>
  <div class="dash left" style="top:568px"></div>
  <div class="item left" style="top:575px"><span class="name">French Toast</span><span class="leader"></span><span class="price">$ 5.49</span></div>
  <p class="detail" style="left:65px;top:598px">Made with homemade bread.</p>
  <div class="dash left" style="top:615px"></div>
  <div class="item left" style="top:626px"><span class="name">French Toast with Meat</span><span class="leader"></span><span class="price">$ 7.49</span></div>
  <div class="dash left" style="top:661px"></div>
  <div class="item left" style="top:673px"><span class="name">Short Stack of Pancakes (3)</span><span class="leader"></span><span class="price">$ 4.99</span></div>
  <div class="dash left" style="top:707px"></div>
  <div class="item left" style="top:719px"><span class="name">Short Stack with Meat</span><span class="leader"></span><span class="price">$ 6.99</span></div>
  <div class="dash left" style="top:754px"></div>
  <p class="note" style="left:57px;top:767px">MEAT CHOICES: SAUSAGE, HAM, BACON, PORKROLL &amp; TURKEY BACON</p>

  <!-- Omelettes -->
  <div class="section-rule left" style="top:794px"></div>
  <h2 class="section-title left" style="top:810px"><span class="flourish" role="img" aria-label="scroll flourish"></span>OMELETTES<span class="flourish" role="img" aria-label="scroll flourish"></span></h2>
  <div class="section-rule left" style="top:855px"></div>
  <p class="note" style="left:57px;top:880px">MADE WITH 3 JUMBO EGGS, SERVED WITH HOME FRIES AND TOAST</p>
  <div class="dash left" style="top:898px"></div>
  <div class="item left" style="top:908px"><span class="name">Cheese Omelette</span><span class="leader"></span><span class="price">$ 6.99</span></div>
  <div class="dash left" style="top:939px"></div>
  <div class="item left" style="top:948px"><span class="name">Bacon &amp; Cheese Omelette</span><span class="leader"></span><span class="price">$ 7.99</span></div>
  <div class="dash left" style="top:979px"></div>
  <div class="item left" style="top:989px"><span class="name">Broccoli &amp; Cheese Omelette</span><span class="leader"></span><span class="price">$ 7.99</span></div>
  <div class="dash left" style="top:1020px"></div>
  <div class="item left" style="top:1029px"><span class="name">Mushroom &amp; Cheese Omelette</span><span class="leader"></span><span class="price">$ 7.99</span></div>
  <div class="dash left" style="top:1060px"></div>
  <div class="item left" style="top:1070px"><span class="name">Western Omelette with Cheese</span><span class="leader"></span><span class="price">$ 7.99</span></div>
  <div class="dash left" style="top:1101px"></div>

  <div class="column-divider"></div>

  <!-- Breakfast special -->
  <div class="section-rule right" style="top:102px"></div>
  <h2 class="section-title right" style="top:117px"><span class="flourish" role="img" aria-label="scroll flourish"></span>BREAKFAST SPECIAL 2X4<span class="flourish" role="img" aria-label="scroll flourish"></span></h2>
  <div class="section-rule right" style="top:163px"></div>
  <div class="dash right" style="top:189px"></div>
  <div class="item right" style="top:198px"><span class="name">2 Pancakes, 2 Eggs, 2 Sausage,</span><span class="leader"></span><span class="price">$ 8.99</span></div>
  <div class="item right" style="top:220px"><span class="name">&amp; 2 Strips of Bacon</span><span class="inline-detail">Served with butter and syrup.</span></div>
  <div class="dash right" style="top:252px"></div>
  <div class="item right minor" style="top:272px"><span class="name">SIDE OF HOME FRIES</span><span class="leader"></span><span class="price">$ 3.99</span></div>
  <div class="item right minor" style="top:294px"><span class="name">SIDE OF HASHBROWNS 2 PCS.</span><span class="leader"></span><span class="price">$ 3.49</span></div>
  <div class="item right minor" style="top:317px"><span class="name">SIDE OF BREAKFAST MEAT</span><span class="leader"></span><span class="price">$ 3.99</span></div>

  <!-- Club sandwiches -->
  <h2 class="banner" style="left:474px;width:375px;top:366px;font-size:38px;">CLUB SANDWICHES</h2>
  <p class="banner-note right" style="top:421px">ALL CLUBS ARE MADE WITH BACON, LETTUCE, TOMATO, AND MAYO<br>ON CHOICE OF TOAST, AND SERVED WITH FRENCH FRIES AND COLESLAW</p>
  <div class="dash right" style="top:474px"></div>
  <div class="item right" style="top:479px"><span class="name">BLT Club</span><span class="leader"></span><span class="price">$ 8.69</span></div>
  <div class="dash right" style="top:509px"></div>
  <div class="item right" style="top:514px"><span class="name">Turkey</span><span class="leader"></span><span class="price">$ 8.69</span></div>
  <div class="dash right" style="top:544px"></div>
  <div class="item right" style="top:550px"><span class="name">Ham &amp; Swiss</span><span class="leader"></span><span class="price">$ 8.69</span></div>
  <div class="dash right" style="top:579px"></div>
  <div class="item right" style="top:585px"><span class="name">Roast Beef &amp; Swiss</span><span class="leader"></span><span class="price">$ 9.49</span></div>
  <div class="dash right" style="top:615px"></div>

  <!-- Soup -->
  <h2 class="banner" style="left:474px;width:375px;top:648px;font-size:38px;gap:20px;">SOUP OF THE DAY</h2>
  <p class="banner-note right" style="top:695px">MADE ON PREMISES AND SERVED WITH CRACKERS<br>SEAFOOD BISQUE, STEWS AND CHILI ARE EXTRA</p>
  <div class="dash right" style="top:747px"></div>
  <div class="item right" style="top:752px"><span class="name">12 Oz. of Soup</span><span class="leader"></span><span class="price">$ 2.99</span></div>
  <div class="dash right" style="top:782px"></div>
  <div class="item right" style="top:788px"><span class="name">16 Oz. of Soup</span><span class="leader"></span><span class="price">$ 3.99</span></div>
  <div class="dash right" style="top:818px"></div>
  <div class="item right" style="top:822px"><span class="name">Quart of Soup</span><span class="leader" style="margin-left:10px"></span><span class="price">$ 7.49</span></div>
  <div class="dash right" style="top:853px"></div>

  <!-- Sides -->
  <h2 class="banner" style="left:472px;width:368px;top:875px;font-size:38px;gap:10px;">SIDES</h2>
  <div class="dash right" style="top:937px"></div>
  <div class="item right" style="top:945px;width:160px"><span class="name">French Fries</span></div>
  <div class="item size" style="left:712px;width:128px;top:941px"><span class="name">Small</span><span class="leader"></span><span class="price">$ 3.99</span></div>
  <div class="item size" style="left:712px;width:128px;top:959px"><span class="name">Large</span><span class="leader"></span><span class="price">$ 7.49</span></div>
  <div class="dash right" style="top:979px"></div>
  <div class="item right" style="top:986px;width:160px"><span class="name">Onion Rings</span></div>
  <div class="item size" style="left:712px;width:128px;top:983px"><span class="name">Small</span><span class="leader"></span><span class="price">$ 4.49</span></div>
  <div class="item size" style="left:712px;width:128px;top:1000px"><span class="name">Large</span><span class="leader"></span><span class="price">$ 8.49</span></div>
  <div class="dash right" style="top:1020px"></div>
  <div class="item right" style="top:1022px"><span class="name">Mozzarella Sticks (6)</span><span class="leader"></span><span class="price">$ 6.99</span></div>
  <p class="detail" style="left:486px;top:1044px">Served with marinara.</p>
  <div class="dash right" style="top:1061px"></div>
  <div class="item right" style="top:1068px"><span class="name">Mac &amp; Cheese</span><span class="leader" style="margin-left:60px"></span><span class="price">$ 7.99</span></div>
  <div class="dash right" style="top:1101px"></div>

  <p class="order-online">ORDER ONLINE @MILLRUNDELI.COM</p>
  <div class="order-bracket"></div>
</main>
</body>
</html>
```